Company brochure for our unique consulting business

We are a small consulting business offering a unique set of services to our clients.. In simple terms we are a business improvement consultancy helping our clients get the best out of their businesses. We work with clients across multiple sectors and deliver a variety of services. We want to put together a brochure to cover these main themes:1. Who we are2. What we do3. The type of people we employ4. The sectors we work inWhile the brochure needs to have a certain corporate feel to it, we don't want it to be "boring" or "stiff". We would like it to have a slightly "friendly" or "informal" feel to it, to reflect the type of organisation we are.We have a company website http://tollandvergeadvisory.com , however we do not want to directly replicate the content or feel as we recognise it needs updating.We would like the brochure to be A4 portrait format. We anticipate requiring 12 sides (including covers) but we are happy to be guided on this based on the content we have provided.The attached ppt file gives the detail of the content to be included and also shows the proposed pagination. For the front cover we would like to try 2 versions, one with the TVA logo and one with the Tolland Verge Advisory logo (a file of both is attached)One of the most important pages will be the "Our Services" page. We would like this to cover the centre fold. In the ppt file we have shown an example layout, but this is where we need most help - we are clearly not graphic designers! This page will be the most used page in sales meetings etc.Also attached is the following:1. file for our TollandVerge Advisory company logo.2. File for our TVA company logo3. Files for Derek's signatures (for under photos) - Owen's to follow4. Photo of Derek & Owen (person in purple shirt to be cropped out)Thank you and really excited to see what everyone comes back with.Derek & Owen

Target Market(s)

Very broad - Manufacturing, Healthcare, Hospitality

Industry/Entity Type

Management Consulting

Font styles to use
Other font styles liked:
• We use Swiss721, but happy to be guided by designer

Colors
3276b5
85abd2
0355a3
333333
5c5c5c
9d9d9d
d9d9d9

Requirements
Must have
• Corporate feel
Nice to have
• Slightly friendly feel
• Our standard "blue" is (CORRECTION) - R55 G96 B146 #376092 and our standard grey is R197 G178, B179 - #B3B2B2, which we would like to keep, but other colours we are happy to be guided on. Brand guidelines attached.

```html
<!DOCTYPE html>
<html lang="en">
<head>
<meta charset="utf-8">
<title>Tolland Verge Advisory – Our Services</title>
<link href="https://fonts.googleapis.com/css2?family=Arimo:wght@400;700&display=swap" rel="stylesheet">
<style>
  :root{
    --brand-blue:#376092;
    --deep-blue:#2f5a8f;
    --ink:#222222;
    --grey-band:#b3b2b2;
    --page:#ffffff;
    --backdrop:#e9e9e9;
    --footer:#111111;
  }
  html,body{margin:0;padding:0;width:1200px;height:1000px;overflow:hidden;background:var(--backdrop);}
  .canvas{position:relative;width:1200px;height:1000px;font-family:"Arimo",Arial,sans-serif;}
  .spread{position:absolute;left:105px;top:150px;width:990px;height:700px;background:var(--page);box-shadow:0 2px 6px rgba(0,0,0,.25);}
  .spread svg{display:block;}
  .page-title{font-size:27px;font-weight:400;fill:var(--ink);}
  .page-title .accent{fill:var(--brand-blue);}
  .title-rule{stroke:var(--brand-blue);stroke-width:1;}
  .connector{stroke:var(--brand-blue);stroke-width:1.3;stroke-dasharray:1.3 3;fill:none;}
  .link{stroke:var(--brand-blue);stroke-width:3.4;stroke-linecap:round;stroke-dasharray:0 6.5;fill:none;}
  .sat-outer{fill:var(--page);stroke:var(--brand-blue);stroke-width:.8;}
  .sat-inner{fill:none;stroke:var(--brand-blue);stroke-width:.5;}
  .sat-label{font-size:6.2px;font-weight:700;fill:var(--brand-blue);text-anchor:middle;letter-spacing:.1px;}
  .hub{fill:var(--brand-blue);}
  .hub-ring{fill:none;stroke:#ffffff;stroke-width:1.2;}
  .hub-title{font-size:11.5px;font-weight:700;fill:#ffffff;text-anchor:middle;}
  .hub-sub{font-size:9px;fill:#ffffff;text-anchor:middle;}
  .intro-band{fill:var(--grey-band);}
  .intro-text{font-size:8.6px;font-weight:700;fill:#ffffff;}
  .folio-bar{fill:var(--footer);}
  .folio-slant{fill:var(--brand-blue);}
  .folio-num{font-size:7px;fill:#ffffff;}
  .gutter-mark{stroke:#cccccc;stroke-width:.8;}
</style>
</head>
<body>
<div class="canvas">
  <div class="spread">
    <svg width="990" height="700" viewBox="105 150 990 700" xmlns="http://www.w3.org/2000/svg">
      <defs>
        <radialGradient id="hubGlow">
          <stop offset="70%" stop-color="#376092" stop-opacity=".35"/>
          <stop offset="100%" stop-color="#376092" stop-opacity="0"/>
        </radialGradient>
      </defs>

      <!-- Heading -->
      <text class="page-title" x="135" y="237">Our <tspan class="accent">Services</tspan></text>
      <line class="title-rule" x1="135" y1="254" x2="215" y2="254"/>

      <line class="gutter-mark" x1="600" y1="607" x2="600" y2="615"/>

      <!-- Links between hubs -->
      <path class="link" d="M440 456 Q600 466 786 434"/>
      <path class="link" d="M438 458 Q430 530 368 582"/>
      <path class="link" d="M370 582 Q520 470 786 434"/>

      <!-- Hub: Organisational Readiness (growth) -->
      <g class="cluster">
        <line class="connector" x1="277" y1="378" x2="402" y2="397"/>
        <line class="connector" x1="304" y1="314" x2="402" y2="397"/>
        <line class="connector" x1="362" y1="273" x2="402" y2="397"/>
        <line class="connector" x1="433" y1="270" x2="402" y2="397"/>
        <line class="connector" x1="494" y1="304" x2="402" y2="397"/>
        <line class="connector" x1="525" y1="367" x2="402" y2="397"/>
        <g><circle class="sat-outer" cx="277" cy="378" r="30"/><circle class="sat-inner" cx="277" cy="378" r="27"/><text class="sat-label" x="277" y="380">MERGER</text></g>
        <g><circle class="sat-outer" cx="304" cy="314" r="30"/><circle class="sat-inner" cx="304" cy="314" r="27"/><text class="sat-label" x="304" y="316">GROWTH</text></g>
        <g><circle class="sat-outer" cx="362" cy="273" r="30"/><circle class="sat-inner" cx="362" cy="273" r="27"/><text class="sat-label" x="362" y="275">OPTIMISATION</text></g>
        <g><circle class="sat-outer" cx="433" cy="270" r="30"/><circle class="sat-inner" cx="433" cy="270" r="27"/><text class="sat-label" x="433" y="272">SALE</text></g>
        <g><circle class="sat-outer" cx="494" cy="304" r="30"/><circle class="sat-inner" cx="494" cy="304" r="27"/><text class="sat-label" x="494" y="306">ACQUISITION</text></g>
        <g><circle class="sat-outer" cx="525" cy="367" r="30"/><circle class="sat-inner" cx="525" cy="367" r="27"/><text class="sat-label" x="525" y="369">SEPARATION</text></g>
        <circle cx="402" cy="397" r="84" fill="url(#hubGlow)"/>
        <circle class="hub" cx="402" cy="397" r="66"/>
        <circle class="hub-ring" cx="402" cy="397" r="59"/>
        <text class="hub-title" x="402" y="385">ORGANISATIONAL<tspan x="402" dy="13">READINESS</tspan></text>
        <text class="hub-sub" x="402" y="411">Getting your business<tspan x="402" dy="10.5">ready for its's future</tspan></text>
      </g>

      <!-- Hub: Programme Management -->
      <g class="cluster">
        <line class="connector" x1="302" y1="498" x2="313" y2="622"/>
        <line class="connector" x1="238" y1="526" x2="313" y2="622"/>
        <line class="connector" x1="192" y1="574" x2="313" y2="622"/>
        <line class="connector" x1="186" y1="642" x2="313" y2="622"/>
        <line class="connector" x1="219" y1="706" x2="313" y2="622"/>
        <line class="connector" x1="276" y1="745" x2="313" y2="622"/>
        <line class="connector" x1="346" y1="745" x2="313" y2="622"/>
        <line class="connector" x1="407" y1="714" x2="313" y2="622"/>
        <line class="connector" x1="438" y1="652" x2="313" y2="622"/>
        <g><circle class="sat-outer" cx="302" cy="498" r="30"/><circle class="sat-inner" cx="302" cy="498" r="27"/><text class="sat-label" x="302" y="492">COST<tspan x="302" dy="7">IMPROVEMENT</tspan><tspan x="302" dy="7">PROGRAMMES</tspan></text></g>
        <g><circle class="sat-outer" cx="238" cy="526" r="30"/><circle class="sat-inner" cx="238" cy="526" r="27"/><text class="sat-label" x="238" y="523">SEPARATION<tspan x="238" dy="7">&amp; MERGER</tspan></text></g>
        <g><circle class="sat-outer" cx="192" cy="574" r="30"/><circle class="sat-inner" cx="192" cy="574" r="27"/><text class="sat-label" x="192" y="572">NEW PRODUCT<tspan x="192" dy="7">INTRODUCTION</tspan></text></g>
        <g><circle class="sat-outer" cx="186" cy="642" r="30"/><circle class="sat-inner" cx="186" cy="642" r="27"/><text class="sat-label" x="186" y="640">I.T. SYSTEM<tspan x="186" dy="7">INTRODUCTION</tspan></text></g>
        <g><circle class="sat-outer" cx="219" cy="706" r="30"/><circle class="sat-inner" cx="219" cy="706" r="27"/><text class="sat-label" x="219" y="704">CUSTOMER<tspan x="219" dy="7">ACCREDITATION</tspan></text></g>
        <g><circle class="sat-outer" cx="276" cy="745" r="30"/><circle class="sat-inner" cx="276" cy="745" r="27"/><text class="sat-label" x="276" y="743">FACILITY<tspan x="276" dy="7">RELOCATION</tspan></text></g>
        <g><circle class="sat-outer" cx="346" cy="745" r="30"/><circle class="sat-inner" cx="346" cy="745" r="27"/><text class="sat-label" x="346" y="743">NEW<tspan x="346" dy="7">EQUIPMENT</tspan></text></g>
        <g><circle class="sat-outer" cx="407" cy="714" r="30"/><circle class="sat-inner" cx="407" cy="714" r="27"/><text class="sat-label" x="407" y="712">MAJOR<tspan x="407" dy="7">EVENTS</tspan></text></g>
        <g><circle class="sat-outer" cx="438" cy="652" r="30"/><circle class="sat-inner" cx="438" cy="652" r="27"/><text class="sat-label" x="438" y="654">ISO</text></g>
        <circle cx="313" cy="622" r="84" fill="url(#hubGlow)"/>
        <circle class="hub" cx="313" cy="622" r="66"/>
        <circle class="hub-ring" cx="313" cy="622" r="59"/>
        <text class="hub-title" x="313" y="603">PROGRAMME<tspan x="313" dy="13">MANAGEMENT</tspan></text>
        <text class="hub-sub" x="313" y="629">Managing programmes<tspan x="313" dy="10.5">through to successful</tspan><tspan x="313" dy="10.5">delivery</tspan></text>
      </g>

      <!-- Hub: Organisational Readiness (people & operations) -->
      <g class="cluster">
        <line class="connector" x1="789" y1="298" x2="853" y2="420"/>
        <line class="connector" x1="853" y1="281" x2="853" y2="420"/>
        <line class="connector" x1="922" y1="298" x2="853" y2="420"/>
        <line class="connector" x1="973" y1="344" x2="853" y2="420"/>
        <line class="connector" x1="997" y1="410" x2="853" y2="420"/>
        <line class="connector" x1="987" y1="477" x2="853" y2="420"/>
        <line class="connector" x1="945" y1="535" x2="853" y2="420"/>
        <line class="connector" x1="884" y1="564" x2="853" y2="420"/>
        <line class="connector" x1="817" y1="570" x2="853" y2="420"/>
        <line class="connector" x1="755" y1="535" x2="853" y2="420"/>
        <line class="connector" x1="716" y1="475" x2="853" y2="420"/>
        <line class="connector" x1="711" y1="405" x2="853" y2="420"/>
        <line class="connector" x1="737" y1="343" x2="853" y2="420"/>
        <g><circle class="sat-outer" cx="789" cy="298" r="30"/><circle class="sat-inner" cx="789" cy="298" r="27"/><text class="sat-label" x="789" y="296">BUSINESS<tspan x="789" dy="7">ASSESSMENT</tspan></text></g>
        <g><circle class="sat-outer" cx="853" cy="281" r="30"/><circle class="sat-inner" cx="853" cy="281" r="27"/><text class="sat-label" x="853" y="280">QUALITY<tspan x="853" dy="7">SYSTEM</tspan></text></g>
        <g><circle class="sat-outer" cx="922" cy="298" r="30"/><circle class="sat-inner" cx="922" cy="298" r="27"/><text class="sat-label" x="922" y="296">STRATEGY<tspan x="922" dy="7">DEVELOPMENT</tspan></text></g>
        <g><circle class="sat-outer" cx="973" cy="344" r="30"/><circle class="sat-inner" cx="973" cy="344" r="27"/><text class="sat-label" x="973" y="338">SENIOR<tspan x="973" dy="7">LEADERSHIP</tspan><tspan x="973" dy="7">DEVELOPMENT</tspan></text></g>
        <g><circle class="sat-outer" cx="997" cy="410" r="30"/><circle class="sat-inner" cx="997" cy="410" r="27"/><text class="sat-label" x="997" y="408">PERSONAL<tspan x="997" dy="7">DEVELOPMENT</tspan></text></g>
        <g><circle class="sat-outer" cx="987" cy="477" r="30"/><circle class="sat-inner" cx="987" cy="477" r="27"/><text class="sat-label" x="987" y="475">SUPPLY CHAIN<tspan x="987" dy="7">DEVELOPMENT</tspan></text></g>
        <g><circle class="sat-outer" cx="945" cy="535" r="30"/><circle class="sat-inner" cx="945" cy="535" r="27"/><text class="sat-label" x="945" y="533">LOGISTICS &amp;<tspan x="945" dy="7">PLANNING</tspan></text></g>
        <g><circle class="sat-outer" cx="884" cy="564" r="30"/><circle class="sat-inner" cx="884" cy="564" r="27"/><text class="sat-label" x="884" y="562">NEW PRODUCT<tspan x="884" dy="7">INTRODUCTION</tspan></text></g>
        <g><circle class="sat-outer" cx="817" cy="570" r="30"/><circle class="sat-inner" cx="817" cy="570" r="27"/><text class="sat-label" x="817" y="568">FACILITY<tspan x="817" dy="7">DESIGN</tspan></text></g>
        <g><circle class="sat-outer" cx="755" cy="535" r="30"/><circle class="sat-inner" cx="755" cy="535" r="27"/><text class="sat-label" x="755" y="533">PROCESS<tspan x="755" dy="7">DESIGN</tspan></text></g>
        <g><circle class="sat-outer" cx="716" cy="475" r="30"/><circle class="sat-inner" cx="716" cy="475" r="27"/><text class="sat-label" x="716" y="469">LEADERSHIP<tspan x="716" dy="7">COACHING &amp;</tspan><tspan x="716" dy="7">MENTORING</tspan></text></g>
        <g><circle class="sat-outer" cx="711" cy="405" r="30"/><circle class="sat-inner" cx="711" cy="405" r="27"/><text class="sat-label" x="711" y="403">ORGANISATIONAL<tspan x="711" dy="7">DESIGN</tspan></text></g>
        <g><circle class="sat-outer" cx="737" cy="343" r="30"/><circle class="sat-inner" cx="737" cy="343" r="27"/><text class="sat-label" x="737" y="341">EQUIPMENT<tspan x="737" dy="7">DESIGN</tspan></text></g>
        <circle cx="853" cy="420" r="84" fill="url(#hubGlow)"/>
        <circle class="hub" cx="853" cy="420" r="66"/>
        <circle class="hub-ring" cx="853" cy="420" r="59"/>
        <text class="hub-title" x="853" y="412">ORGANISATIONAL<tspan x="853" dy="13">READINESS</tspan></text>
        <text class="hub-sub" x="853" y="438">Getting your business<tspan x="853" dy="10.5">ready for its's future</tspan></text>
      </g>

      <!-- Intro band -->
      <polygon class="intro-band" points="541,662 1085,662 1025,792 482,792"/>
      <text class="intro-text" x="645" y="709">We recognise every organisation we work with is different; the products or
        <tspan x="645" dy="11">services provided, the culture and the readiness for change but most</tspan>
        <tspan x="645" dy="11">importantly the ‘wants and needs’ are always unique. The skills, knowledge</tspan>
        <tspan x="645" dy="11">and experience across our team means we are able to offer an extensive</tspan>
        <tspan x="645" dy="11">range of services which are tailored to meet your specific needs.</tspan>
      </text>

      <!-- Folios -->
      <rect class="folio-bar" x="105" y="803" width="45" height="11"/>
      <polygon class="folio-slant" points="153,803 164,803 157,814 146,814"/>
      <text class="folio-num" x="134" y="811.5">6</text>
      <polygon class="folio-slant" points="1043,803 1054,803 1047,814 1036,814"/>
      <rect class="folio-bar" x="1051" y="803" width="44" height="11"/>
      <text class="folio-num" x="1062" y="811.5">7</text>
    </svg>
  </div>
</div>
</body>
</html>
```